Membership Sales Page Web Design

We need a website designed to showcase the benefits of joining our online community of technology procurement professionals.

Our community has been around for a while and it's time for a refresh. Included in the brief is Verson 1.0 of the site. You can see the current version of the site @ brindlehub.com.

As part of the refresh, we've acquired a new primary domain name (brindle.com) and will be rolling out both a free and paid subscription model.

Because of this, there should be a strong call to sign (join now) infused within the site.

We would like to see site designs that are clean, flat and minimalistic in nature. Our membership colors are royal blue, grey, and white.

The final design should communicate networking and professional growth.

I'd be particularly interestedin seeing some flat website designs with a strong call to action. Here are some great examples for inspiration:

https://pivotlyst.com/
https://marrowkit.io/

Target Market(s)

vantage 400 companies

Number of Pages Required

1 page

Font styles to use
Sans Serif

Colors
0293ce
3276b5
ffffff

Requirements
Must have
• clean, minimalistic, fee
strong call to action
showcase our different membership levels
highlight the benefits of membership
Nice to have
• n/a
Should not have
• n/a

```html
<!DOCTYPE html>
<html lang="en">
<head>
<meta charset="utf-8">
<title>BRINDLE – IT Procurement Community</title>
<link href="https://fonts.googleapis.com/css2?family=Oswald:wght@400;500&family=Roboto:wght@400;500;700&display=swap" rel="stylesheet">
<style>
:root{
  --blue:#3276b5;
  --sky:#0293ce;
  --white:#ffffff;
  --ink:#2a2f36;
  --text:#5d636b;
  --muted:#8a9097;
  --line:#e2e5e9;
  --grey-bg:#ededed;
  --footer:#2b2d30;
  --footer-deep:#222326;
}
*{box-sizing:border-box;margin:0;padding:0}
html,body{width:1200px;height:3548px;overflow:hidden}
body{font-family:"Roboto",Arial,sans-serif;color:var(--text);background:var(--white);position:relative}
a{color:inherit;text-decoration:none}
.heading{font-family:"Oswald","Arial Narrow",sans-serif;font-weight:400;color:var(--ink)}
.btn{display:inline-block;background:var(--blue);color:var(--white);font-size:15px;font-weight:500;padding:0 34px;height:52px;line-height:52px;border-radius:2px}

/* header */
.site-header{position:absolute;top:0;left:0;width:1200px;height:58px;background:var(--white)}
.brand{position:absolute;left:28px;top:0;height:58px;line-height:58px;font-size:30px;font-weight:700;letter-spacing:1px;color:var(--blue)}
.topbar{position:absolute;right:36px;top:6px;display:flex;align-items:center;gap:14px;font-size:10px;color:var(--muted)}
.topbar .phone{color:var(--blue);font-weight:700;font-size:13px}
.social{display:flex;gap:6px}
.social span{width:18px;height:18px;border-radius:50%;background:var(--blue);display:block}
.main-nav{position:absolute;right:36px;top:34px;display:flex;align-items:center;gap:18px;font-size:12px;color:var(--ink)}
.main-nav .login{background:var(--blue);color:var(--white);padding:5px 12px;border-radius:2px}

/* hero */
.hero{position:absolute;top:58px;left:0;width:1200px;height:604px}
.hero-photo{position:absolute;inset:0;background:linear-gradient(100deg,#8fa3b3 0%,#d9d5cc 30%,#efece6 55%,#c9b9a3 80%,#a89680 100%)}
.hero-card{position:absolute;left:380px;top:60px;width:440px;height:312px;background:rgba(255,255,255,.9);text-align:center;padding-top:44px}
.hero-card h1{font-family:"Oswald",sans-serif;font-weight:400;font-size:30px;color:var(--ink)}
.hero-card h2{font-family:"Oswald",sans-serif;font-weight:500;font-size:44px;color:var(--blue);letter-spacing:1px;line-height:1.1}
.hero-card p{font-size:11px;color:var(--muted);margin:14px 0 26px}

/* about */
.about{position:absolute;top:662px;left:0;width:1200px;height:698px;text-align:center}
.section-title{font-size:38px;padding-top:96px}
.section-title::after{content:"";display:block;width:60px;height:3px;background:var(--blue);margin:10px auto 0}
.about .lead{font-size:13px;color:var(--text);margin-top:10px}
.features{position:absolute;top:258px;left:218px;width:780px;display:grid;grid-template-columns:1fr 1fr;column-gap:70px;row-gap:64px;text-align:left}
.feature{display:flex;gap:22px}
.feature svg{flex:none}
.feature h3{font-family:"Oswald",sans-serif;font-weight:400;font-size:20px;color:var(--ink);margin-bottom:8px}
.feature p{font-size:11px;line-height:1.55;color:var(--text);width:220px}

/* membership */
.member-photo{position:absolute;top:1360px;left:0;width:1200px;height:480px;background:linear-gradient(95deg,#d8c9a8 0%,#efe6d6 30%,#c7cfd6 55%,#e7ddcc 75%,#b9c1c9 100%)}
.member-card{position:absolute;top:1660px;left:600px;width:560px;height:680px;background:var(--white);padding:56px 12px 0 18px}
.member-card h2{font-size:38px}
.member-card h2::after{content:"";display:block;width:60px;height:3px;background:var(--blue);margin-top:10px}
.member-card .intro{font-size:12px;line-height:1.6;margin:18px 0 20px;width:420px}
.benefits{list-style:none}
.benefits li{display:flex;align-items:center;gap:12px;font-size:13px;color:var(--ink);height:33px}
.benefits li svg{flex:none}
.member-card .btn{margin-top:26px}

.quick-links{position:absolute;top:1848px;left:200px;width:300px}
.quick-links h2{font-size:38px}
.quick-links h2::after{content:"";display:block;width:60px;height:3px;background:var(--blue);margin-top:8px}
.quick-links ul{list-style:none;margin-top:24px}
.quick-links li{font-size:12px;color:var(--blue);height:34px}

/* pricing */
.pricing{position:absolute;top:2370px;left:0;width:1200px;height:820px;background:var(--grey-bg);text-align:center}
.pricing .section-title{padding-top:82px}
.plan{position:absolute;background:var(--white);text-align:center}
.plan.free{left:140px;top:234px;height:530px;width:280px}
.plan.standard{left:452px;top:210px;height:580px;width:300px}
.plan.plus{left:772px;top:234px;height:530px;width:290px}
.plan h3{font-size:20px;font-weight:500;color:var(--ink);padding-top:40px}
.plan.standard h3{padding-top:56px}
.plan .price{font-family:"Oswald",sans-serif;font-size:40px;color:var(--blue);margin-top:40px;border-top:1px solid var(--line);padding-top:24px;margin-left:20px;margin-right:20px}
.plan .per{font-size:11px;color:var(--muted);border-bottom:1px solid var(--line);padding-bottom:22px;margin:0 20px}
.plan ul{list-style:none;margin:26px 0 26px}
.plan li{font-size:11px;color:var(--text);height:30px;line-height:30px;border-bottom:1px solid #f1f2f4;margin:0 50px}
.plan .btn{width:180px;padding:0}

/* footer */
.site-footer{position:absolute;top:3190px;left:0;width:1200px;height:358px;background:var(--footer);color:#c9ccd0}
.footer-brand{position:absolute;left:150px;top:56px}
.footer-brand strong{font-size:38px;font-weight:700;color:var(--sky);letter-spacing:1px}
.footer-brand p{font-size:11px;line-height:1.6;width:220px;margin-top:8px}
.footer-col{position:absolute;top:64px}
.footer-col h4{font-size:14px;font-weight:500;color:var(--white);margin-bottom:14px}
.footer-col li{list-style:none;font-size:11px;height:22px}
.copyright{position:absolute;left:0;bottom:0;width:1200px;height:60px;background:var(--footer-deep);font-size:12px;line-height:60px;padding-left:150px}
.copyright .social{position:absolute;right:140px;top:20px}
.copyright .social span{background:var(--sky)}
</style>
</head>
<body>

<header class="site-header">
  <a class="brand" href="#">BRINDLE</a>
  <div class="topbar">
    <svg width="14" height="14" viewBox="0 0 24 24"><path fill="#3276b5" d="M6.6 10.8a15 15 0 0 0 6.6 6.6l2.2-2.2a1 1 0 0 1 1-.25 11.4 11.4 0 0 0 3.6.57 1 1 0 0 1 1 1V20a1 1 0 0 1-1 1A17 17 0 0 1 3 4a1 1 0 0 1 1-1h3.5a1 1 0 0 1 1 1c0 1.25.2 2.45.57 3.57a1 1 0 0 1-.25 1z"/></svg>
    <span class="phone">1-800-555-0142</span>
    <span>Join a Network | Meet Blog | FAQ | Login</span>
    <div class="social"><span></span><span></span><span></span></div>
  </div>
  <nav class="main-nav">
    <a href="#">Featured Events</a><a href="#">Offerings</a><a href="#">Shop</a><a href="#">Certification</a><a class="login" href="#">Member Login</a>
  </nav>
</header>

<section class="hero">
  <div class="hero-photo" role="img" aria-label="Photo of two business colleagues bumping fists in a bright office"></div>
  <div class="hero-card">
    <h1>IT Procurement summit</h1>
    <h2>BRINDLE</h2>
    <p>Join peers who shape smart buying decisions every year.</p>
    <a class="btn" href="#">Learn More</a>
  </div>
</section>

<section class="about">
  <h2 class="heading section-title">Promoting excellence acquisition profesionals</h2>
  <p class="lead">Lorem ipsum dolor sit amet, consectetur adipiscing elit.</p>
  <div class="features">
    <div class="feature">
      <svg width="40" height="40" viewBox="0 0 40 40" fill="none" stroke="#3276b5" stroke-width="1.5"><circle cx="17" cy="17" r="11"/><path d="M25 25l10 10"/></svg>
      <div><h3>What is brindle</h3><p>Lorem ipsum dolor sit amet, consectetur adipiscing elit, sed diam nonummy tempor incidunt ut labore et dolore magna aliquam erat, sed diam voluptua.</p></div>
    </div>
    <div class="feature">
      <svg width="40" height="40" viewBox="0 0 40 40" fill="none" stroke="#3276b5" stroke-width="1.5"><circle cx="20" cy="20" r="16"/><path d="M4 20h32M20 4c6 5 6 27 0 32M20 4c-6 5-6 27 0 32"/></svg>
      <div><h3>Who is brindle</h3><p>Lorem ipsum dolor sit amet, consectetur adipiscing elit, sed diam nonummy tempor incidunt ut labore et dolore magna aliquam erat, sed diam voluptua.</p></div>
    </div>
    <div class="feature">
      <svg width="40" height="40" viewBox="0 0 40 40" fill="none" stroke="#3276b5" stroke-width="1.5"><circle cx="20" cy="20" r="16"/><circle cx="20" cy="20" r="9"/><circle cx="20" cy="20" r="2"/></svg>
      <div><h3>What is its mission</h3><p>Lorem ipsum dolor sit amet, consectetur adipiscing elit, sed diam nonummy tempor incidunt ut labore et dolore magna aliquam erat, sed diam voluptua.</p></div>
    </div>
    <div class="feature">
      <svg width="40" height="40" viewBox="0 0 40 40" fill="none" stroke="#3276b5" stroke-width="1.5"><path d="M6 30l9-9 6 6 13-13"/><path d="M26 14h8v8"/></svg>
      <div><h3>Why should i join?</h3><p>Lorem ipsum dolor sit amet, consectetur adipiscing elit, sed diam nonummy tempor incidunt ut labore et dolore magna aliquam erat, sed diam voluptua.</p></div>
    </div>
  </div>
</section>

<div class="member-photo" role="img" aria-label="Photo of smiling colleagues gathered around a laptop in an office"></div>

<aside class="quick-links">
  <h2 class="heading">Quick link</h2>
  <ul>
    <li>Vendor live discussion News</li><li>Vendor comments</li><li>Document library</li><li>Election index</li><li>Course events</li><li>Certification</li><li>Career center</li>
  </ul>
</aside>

<section class="member-card">
  <h2 class="heading">Become a member today</h2>
  <p class="intro">Lorem ipsum dolor sit amet, consectetur adipiscing elit, sed diam nonummy tempor incidunt ut labore et dolore magna aliquam erat, sed diam voluptua. At vero eos et accusam.</p>
  <ul class="benefits">
    <li><svg width="18" height="18" viewBox="0 0 18 18"><circle cx="9" cy="9" r="8" fill="none" stroke="#3276b5"/><path d="M5 9l3 3 5-6" fill="none" stroke="#3276b5" stroke-width="1.5"/></svg>Work smart</li>
    <li><svg width="18" height="18" viewBox="0 0 18 18"><circle cx="9" cy="9" r="8" fill="none" stroke="#3276b5"/><path d="M5 9l3 3 5-6" fill="none" stroke="#3276b5" stroke-width="1.5"/></svg>Do better deals</li>
    <li><svg width="18" height="18" viewBox="0 0 18 18"><circle cx="9" cy="9" r="8" fill="none" stroke="#3276b5"/><path d="M5 9l3 3 5-6" fill="none" stroke="#3276b5" stroke-width="1.5"/></svg>Gain valuable skills</li>
    <li><svg width="18" height="18" viewBox="0 0 18 18"><circle cx="9" cy="9" r="8" fill="none" stroke="#3276b5"/><path d="M5 9l3 3 5-6" fill="none" stroke="#3276b5" stroke-width="1.5"/></svg>Advance your career</li>
    <li><svg width="18" height="18" viewBox="0 0 18 18"><circle cx="9" cy="9" r="8" fill="none" stroke="#3276b5"/><path d="M5 9l3 3 5-6" fill="none" stroke="#3276b5" stroke-width="1.5"/></svg>Counter vendor ploys</li>
    <li><svg width="18" height="18" viewBox="0 0 18 18"><circle cx="9" cy="9" r="8" fill="none" stroke="#3276b5"/><path d="M5 9l3 3 5-6" fill="none" stroke="#3276b5" stroke-width="1.5"/></svg>Save time, money and aggravations</li>
    <li><svg width="18" height="18" viewBox="0 0 18 18"><circle cx="9" cy="9" r="8" fill="none" stroke="#3276b5"/><path d="M5 9l3 3 5-6" fill="none" stroke="#3276b5" stroke-width="1.5"/></svg>Share working solutions to real situations</li>
    <li><svg width="18" height="18" viewBox="0 0 18 18"><circle cx="9" cy="9" r="8" fill="none" stroke="#3276b5"/><path d="M5 9l3 3 5-6" fill="none" stroke="#3276b5" stroke-width="1.5"/></svg>Interact with your peer about vendors</li>
  </ul>
  <a class="btn" href="#">Learn More</a>
</section>

<section class="pricing">
  <h2 class="heading section-title">Our pricing packages</h2>
  <div class="plan free">
    <h3>Free</h3>
    <div class="price">$00.00</div><div class="per">Per user per month</div>
    <ul><li>10 projects</li><li>Enhanced Security</li><li>5 GB Storage</li><li>Unlimited Users</li><li>Per Time Tracking</li><li>Enhanced Security</li></ul>
    <a class="btn" href="#">Learn More</a>
  </div>
  <div class="plan standard">
    <h3>Standard</h3>
    <div class="price">$15.00</div><div class="per">Per user per month</div>
    <ul><li>10 projects</li><li>Enhanced Security</li><li>5 GB Storage</li><li>Unlimited Users</li><li>Per Time Tracking</li><li>Enhanced Security</li></ul>
    <a class="btn" href="#">Learn More</a>
  </div>
  <div class="plan plus">
    <h3>Plus</h3>
    <div class="price">$29.00</div><div class="per">Per user per month</div>
    <ul><li>10 projects</li><li>Enhanced Security</li><li>5 GB Storage</li><li>Unlimited Users</li><li>Per Time Tracking</li><li>Enhanced Security</li></ul>
    <a class="btn" href="#">Learn More</a>
  </div>
</section>

<footer class="site-footer">
  <div class="footer-brand"><strong>BRINDLE</strong><p>Lorem ipsum dolor sit amet, consectetur adipiscing elit, sed diam nonummy tempor incidunt.</p></div>
  <div class="footer-col" style="left:520px"><h4>Learn about BRINDLE</h4><ul><li>Home</li><li>Join BRINDLE</li><li>Your BRINDLE</li><li>Announcement</li></ul></div>
  <div class="footer-col" style="left:730px"><h4>Attend an Event</h4><ul><li>IT Procurement summit</li><li>Event &amp; Workshops</li><li>Online Seminars</li><li>Regional Workshops</li></ul></div>
  <div class="footer-col" style="left:920px"><h4>Connect with BRINDLE</h4><ul><li>Use this conference App</li><li>Contact us</li></ul></div>
  <div class="copyright">Copyright © 2020 BRINDLE<div class="social"><span></span><span></span><span></span></div></div>
</footer>

</body>
</html>
```